Pest control truck wrap

Needing an eye catching wrap for my new work truck. Its a 2018 Varnell Marbeck QD Stretch Cab with a Hallix 240vkt canopy. It needs to stand out and be eye catching but not too busy, I want people to know who I am and what I'm doing. It also needs to be easily adaptable to my older trucks, which are full size without canopies. I prefer solid colors, probably black, white and green, and maybe a little orange. My logo should be large enough that it can be easily read from a distance, but not so big it takes up the whole truck. Since this is a pest control truck, it should communicate that. Bear in mind we primarily do insect and spider control, not rodents or wildlife. I'll include photos of the new truck, my logo, and one of my older trucks for reference.

```html
<!DOCTYPE html>
<html lang="en">
<head>
<meta charset="utf-8">
<title>Kestrel Weed and Pest Control – Truck Wrap</title>
<link href="https://fonts.googleapis.com/css2?family=Oswald:wght@600;700&family=Russo+One&display=swap" rel="stylesheet">
<style>
  :root {
    --paper: #ffffff;
    --ink: #111111;
    --wrap-dark: #1b1d1e;
    --wrap-mid: #2c3032;
    --accent: #ef7a17;
    --line: #6b6b6b;
  }
  html, body {
    margin: 0;
    width: 1200px;
    height: 1200px;
    overflow: hidden;
    background: var(--paper);
  }
  .canvas {
    width: 1200px;
    height: 1200px;
    display: flex;
    align-items: center;
    justify-content: center;
  }
  .wrap-template { width: 1200px; height: auto; display: block; }
  .outline { fill: var(--paper); stroke: var(--line); stroke-width: 1.5; }
  .glass { fill: var(--paper); stroke: var(--ink); stroke-width: 1.5; }
  .panel-dark { fill: url(#hexTone); }
  .band { fill: var(--accent); }
  .brand-name {
    font-family: "Oswald", sans-serif;
    font-weight: 700;
    font-size: 64px;
    fill: var(--ink);
  }
  .brand-sub {
    font-family: "Oswald", sans-serif;
    font-weight: 600;
    font-size: 17px;
    fill: var(--ink);
  }
  .brand-phone {
    font-family: "Oswald", sans-serif;
    font-weight: 600;
    font-size: 26px;
    fill: var(--ink);
  }
  .brand-mark { fill: none; stroke: var(--ink); stroke-width: 5; }
  .service-line {
    font-family: "Russo One", sans-serif;
    font-style: italic;
    font-size: 36px;
    fill: var(--paper);
  }
  .service-phone {
    font-family: "Oswald", sans-serif;
    font-weight: 700;
    font-size: 42px;
    fill: var(--accent);
  }
  .phone-icon { fill: none; stroke: var(--accent); stroke-width: 3; stroke-linecap: round; }
  .no-bug-ring { fill: var(--wrap-dark); stroke: var(--accent); stroke-width: 5; }
  .no-bug-slash { stroke: var(--accent); stroke-width: 5; stroke-linecap: round; }
  .no-bug-fill { fill: var(--accent); opacity: .35; }
</style>
</head>
<body>
<main class="canvas">
  <svg class="wrap-template" viewBox="150 100 1500 410" xmlns="http://www.w3.org/2000/svg">
    <defs>
      <linearGradient id="hexTone" x1="0" y1="0" x2="0" y2="1">
        <stop offset="0" stop-color="#3a3f41"/>
        <stop offset=".5" stop-color="#25292b"/>
        <stop offset="1" stop-color="#141617"/>
      </linearGradient>
    </defs>

    <g class="cab">
      <path class="outline" d="M1025 120 L820 113 Q700 113 620 140 Q560 170 505 250 L330 256 L200 275 L175 290 L215 300 L180 330 L225 390 Q300 360 380 365 Q440 375 465 430 L480 488 L1025 488 Z"/>
      <polygon class="panel-dark" role="img" aria-label="Dark hexagon texture panel" points="960,118 1025,120 1025,488 780,488"/>
      <polygon class="band" points="925,117 962,118 780,488 720,488"/>
      <path class="glass" d="M560 240 Q600 170 680 150 L820 140 Q828 140 828 148 L825 258 Q825 265 818 265 L560 267 Q545 265 560 240 Z"/>
      <rect class="glass" x="862" y="140" width="122" height="126" rx="12"/>

      <g class="brand-lockup">
        <circle class="brand-mark" cx="545" cy="395" r="50"/>
        <text class="brand-sub" x="610" y="336">Weed and Pest Control</text>
        <text class="brand-name" x="606" y="400">Kestrel</text>
        <text class="brand-phone" x="608" y="438">(208) 555-0147</text>
      </g>
    </g>

    <g class="bed">
      <path class="panel-dark" role="img" aria-label="Dark hexagon texture panel" d="M1035 120 L1520 122 Q1560 125 1580 170 L1600 230 L1622 262 L1605 290 L1590 320 L1585 470 L1435 480 C1432 420 1395 392 1320 392 C1240 392 1195 425 1185 470 L1175 488 L1040 488 Q1030 300 1035 120 Z"/>
      <rect class="glass" x="1080" y="143" width="470" height="102" rx="24"/>

      <g transform="rotate(-6 1065 300)">
        <text class="service-line" x="1068" y="292">WEED AND</text>
        <text class="service-line" x="1068" y="330">PEST CONTROL</text>
        <text class="service-phone" x="1100" y="374">(208) 555-0147</text>
        <path class="phone-icon" d="M1062 350 q-6 10 4 20 q10 8 18 2 M1072 346 a10 10 0 0 1 10 10 M1072 338 a18 18 0 0 1 18 18"/>
      </g>

      <g class="no-bug" role="img" aria-label="No ants sign">
        <circle class="no-bug-ring" cx="1435" cy="316" r="27"/>
        <circle class="no-bug-fill" cx="1435" cy="316" r="14"/>
        <line class="no-bug-slash" x1="1416" y1="297" x2="1454" y2="335"/>
      </g>
      <g class="no-bug" role="img" aria-label="No mosquitoes sign">
        <circle class="no-bug-ring" cx="1514" cy="296" r="35"/>
        <circle class="no-bug-fill" cx="1514" cy="296" r="18"/>
        <line class="no-bug-slash" x1="1489" y1="271" x2="1539" y2="321"/>
      </g>
      <g class="no-bug" role="img" aria-label="No ticks sign">
        <circle class="no-bug-ring" cx="1497" cy="380" r="31"/>
        <circle class="no-bug-fill" cx="1497" cy="380" r="16"/>
        <line class="no-bug-slash" x1="1475" y1="358" x2="1519" y2="402"/>
      </g>
    </g>
  </svg>
</main>
</body>
</html>
```